Newspaper Ad - New Veterinarian Introduction

I am looking to create a standard Newspaper ad that l can use as a template to introduce new Veterinarians (when they join our practice) to the local community.

The goal is to create an ad that captures the reader's eye, creates a warm emotional connection with the vet, and that encourages the reader to think of our clinic when they have veterinary needs.

Target Market(s)

Pet owners

Industry/Entity Type

Veterinary

Requirements
Must have
• The ad will contain a photo of the vet (sample phone attached) and a short bio of their interests and/or specialties.

The ad will also include basic contact information on the clinic: logo, phone, website, email
Nice to have
• Optional information could include:
- Like us on pinmesh
- features of the clinic (e.g. feline friendly room)
- other vets who work at the clinic

```html
<!DOCTYPE html>
<html lang="en">
<head>
<meta charset="utf-8">
<title>Cedar Bluff Animal Hospital – New Veterinarian Ad</title>
<link href="https://fonts.googleapis.com/css2?family=Roboto+Condensed:wght@400;700;800&display=swap" rel="stylesheet">
<style>
:root{
  --navy:#1d3a8f;
  --sky:#2aa3e2;
  --red:#c1251f;
  --yellow:#f6e400;
  --white:#ffffff;
  --paper:#f1f2f4;
  --stage:#262626;
  --frame:#d9d9d9;
}
*{box-sizing:border-box;margin:0;padding:0}
html,body{width:1200px;height:944px;overflow:hidden}
body{background:var(--stage);position:relative;font-family:"Roboto Condensed","Arial Narrow",sans-serif;font-weight:700}
.ad{position:absolute;top:72px;width:462px;height:787px;background:var(--white);overflow:hidden;--accent:var(--navy)}
.ad--blue{left:110px}
.ad--red{left:606px;--accent:var(--red)}
.ad__band{position:absolute;left:0;top:140px;width:462px;height:170px}
.brand{position:absolute;left:34px;top:26px;display:flex;align-items:center;gap:10px}
.brand__mark{width:52px;height:52px;border-radius:50%;background:var(--sky)}
.brand__name{color:var(--navy);font-weight:800;font-size:21px;line-height:1.05;text-transform:uppercase;width:150px}
.portrait{position:absolute;left:243px;top:21px;width:198px;height:212px;background:var(--frame);padding:8px}
.portrait__photo{width:100%;height:100%;background:linear-gradient(160deg,#d9c6b0 0%,#b9704a 45%,#3b3140 100%)}
.contact{position:absolute;left:76px;top:136px;list-style:none;color:var(--navy);font-size:13.5px;line-height:20.5px}
.contact li{display:flex;align-items:center;gap:6px}
.contact svg{width:11px;height:11px}
.headline{position:absolute;left:0;top:254px;width:462px;text-align:center;color:var(--white);font-size:20px;line-height:23px}
.bio{position:absolute;left:12px;top:313px;width:438px;color:var(--navy);font-size:15px;letter-spacing:0.5px;line-height:19.5px;text-align:justify}
.lead{position:absolute;left:12px;top:478px;color:var(--navy);font-size:15px;letter-spacing:0.3px}
.pets{position:absolute;left:14px;top:498px;display:flex;gap:10px}
.pets__pet{width:56px;height:88px;border-radius:28px 28px 6px 6px}
.pet--cat{background:linear-gradient(#f0a050,#d9782a)}
.pet--dog{background:linear-gradient(#efe6d2,#cfc2a4)}
.pet--rabbit{background:linear-gradient(#f7f7f7,#d6d6d6)}
.assure{position:absolute;left:251px;top:513px;width:211px;height:68px;background:var(--accent);color:var(--white);font-size:15px;letter-spacing:0.3px;line-height:19px;padding:6px 14px}
.news{position:absolute;left:0;top:593px;width:462px;height:81px;background:var(--navy);color:var(--white);font-size:14px;letter-spacing:0.3px;line-height:18px;padding:5px 12px;text-align:justify}
.news em{font-style:normal;color:var(--yellow)}
.team{position:absolute;left:0;top:674px;width:462px;height:46px;color:var(--navy);font-size:15.5px;letter-spacing:0.3px;line-height:20px;text-align:center;padding-top:3px}
.ad--red .team{background:var(--red);color:var(--white)}
.footer{position:absolute;left:0;top:720px;width:462px;height:67px;background:var(--navy);color:var(--white)}
.footer__slug{position:absolute;left:12px;top:7px;font-size:12.5px;letter-spacing:0.2px;line-height:14.5px}
.social{position:absolute;left:324px;top:12px;width:126px;height:36px;background:var(--sky);display:flex;align-items:center;gap:8px;padding:0 8px;color:var(--white);font-size:13px;line-height:13px}
.social__dot{width:22px;height:22px;background:var(--white);border-radius:3px;flex:none}
</style>
</head>
<body>

<section class="ad ad--blue">
  <svg class="ad__band" viewBox="0 0 462 170" aria-hidden="true">
    <path d="M0 40 C120 80 300 95 462 60 L462 170 L0 170 Z" fill="var(--navy)"/>
    <path d="M0 0 L240 0 L240 100 C160 112 80 104 0 85 Z" fill="var(--white)"/>
  </svg>
  <div class="brand"><span class="brand__mark"></span><span class="brand__name">Cedar Bluff Animal Hospital</span></div>
  <div class="portrait"><div class="portrait__photo" role="img" aria-label="Photo of the new veterinarian holding a black and white rabbit"></div></div>
  <ul class="contact">
    <li><svg viewBox="0 0 12 12"><rect x="1" y="3" width="10" height="7" rx="1" fill="var(--navy)"/></svg>780-555-0147</li>
    <li><svg viewBox="0 0 12 12"><circle cx="6" cy="6" r="5" fill="var(--navy)"/></svg>info@cedarbluffvet.com</li>
    <li><svg viewBox="0 0 12 12"><circle cx="6" cy="6" r="5" fill="var(--navy)"/></svg>www.cedarbluffvet.com</li>
  </ul>
  <h1 class="headline">Cedar Bluff Animal Hospital is pleased to welcome<br>Dr. Megan Harlow to our practice.</h1>
  <p class="bio">Graduating from the Prairie College of Veterinary Medicine in Saskatoon in 2002, Dr. Harlow has over 10 years of veterinary experience. Her love and care for animals extends beyond work to her home and through her volunteer work at the local wildlife rehabilitation centre. Dr. Harlow loves the challenges and diversity that a general veterinary clinic brings and has a special interest in internal medicine, dentistry and improving the quality of life for aging pets.</p>
  <p class="lead">So whether your companion is</p>
  <div class="pets">
    <div class="pets__pet pet--cat" role="img" aria-label="Ginger kitten"></div>
    <div class="pets__pet pet--dog" role="img" aria-label="White terrier"></div>
    <div class="pets__pet pet--rabbit" role="img" aria-label="White and black rabbit"></div>
  </div>
  <p class="assure">You can rest assured your pet is in good hands with Dr. Harlow.</p>
  <p class="news">Cedar Bluff now has a <em>pinmesh</em> page where you can follow interesting stories and see patient experiences. Sign on and “Like” us today. <em>Feline Friendly Room</em> At Cedar Bluff we appreciate how stressful a visit to the Vet can be to a cat...we now have a Feline Friendly Room.</p>
  <p class="team">Dr. Laura Bennick, Dr. Dana Koval,<br>Dr. Erin Malloy, and Dr. Clara Dunmore</p>
  <footer class="footer">
    <p class="footer__slug">WED. GAZ., JAN 23/13 – 1/4 (process)<br>JA: CEDAR BLUFF ANIMAL HOSPITAL (H3)<br>SALES: SHELBY<br>27134</p>
    <div class="social"><span class="social__dot"></span><span>Like us on<br>pinmesh</span></div>
  </footer>
</section>

<section class="ad ad--red">
  <svg class="ad__band" viewBox="0 0 462 170" aria-hidden="true">
    <path d="M0 40 C120 80 300 95 462 60 L462 170 L0 170 Z" fill="var(--navy)"/>
    <path d="M0 0 L240 0 L240 100 C160 112 80 104 0 85 Z" fill="var(--white)"/>
  </svg>
  <div class="brand"><span class="brand__mark"></span><span class="brand__name">Cedar Bluff Animal Hospital</span></div>
  <div class="portrait"><div class="portrait__photo" role="img" aria-label="Photo of the new veterinarian holding a black and white rabbit"></div></div>
  <ul class="contact">
    <li><svg viewBox="0 0 12 12"><rect x="1" y="3" width="10" height="7" rx="1" fill="var(--navy)"/></svg>780-555-0147</li>
    <li><svg viewBox="0 0 12 12"><circle cx="6" cy="6" r="5" fill="var(--navy)"/></svg>info@cedarbluffvet.com</li>
    <li><svg viewBox="0 0 12 12"><circle cx="6" cy="6" r="5" fill="var(--navy)"/></svg>www.cedarbluffvet.com</li>
  </ul>
  <h1 class="headline">Cedar Bluff Animal Hospital is pleased to welcome<br>Dr. Megan Harlow to our practice.</h1>
  <p class="bio">Graduating from the Prairie College of Veterinary Medicine in Saskatoon in 2002, Dr. Harlow has over 10 years of veterinary experience. Her love and care for animals extends beyond work to her home and through her volunteer work at the local wildlife rehabilitation centre. Dr. Harlow loves the challenges and diversity that a general veterinary clinic brings and has a special interest in internal medicine, dentistry and improving the quality of life for aging pets.</p>
  <p class="lead">So whether your companion is</p>
  <div class="pets">
    <div class="pets__pet pet--cat" role="img" aria-label="Ginger kitten"></div>
    <div class="pets__pet pet--dog" role="img" aria-label="White terrier"></div>
    <div class="pets__pet pet--rabbit" role="img" aria-label="White and black rabbit"></div>
  </div>
  <p class="assure">You can rest assured your pet is in good hands with Dr. Harlow.</p>
  <p class="news">Cedar Bluff now has a <em>pinmesh</em> page where you can follow interesting stories and see patient experiences. Sign on and “Like” us today. <em>Feline Friendly Room</em> At Cedar Bluff we appreciate how stressful a visit to the Vet can be to a cat...we now have a Feline Friendly Room.</p>
  <p class="team">Dr. Laura Bennick, Dr. Dana Koval,<br>Dr. Erin Malloy, and Dr. Clara Dunmore</p>
  <footer class="footer">
    <p class="footer__slug">WED. GAZ., JAN 23/13 – 1/4 (process)<br>JA: CEDAR BLUFF ANIMAL HOSPITAL (H3)<br>SALES: SHELBY<br>27134</p>
    <div class="social"><span class="social__dot"></span><span>Like us on<br>pinmesh</span></div>
  </footer>
</section>

</body>
</html>
```